Brochure Design Project

Color brochure with text, graphics, and photos. (I will provide the text). 4 pages of 8 1/2 X 11". This is a brochure about dental implants.
Attached is the text and logo for the brochure.

See new parameters and information on the brochure project.

Included in the brochure is our address: Brookfield Dental Care, 218 Larchmont Avenue, Brookfield, PA 17342.  717-482-6915.  www.brookfielddentalcare-example.com.

Martin R. Pulaski, D.M.D., M.A.G.D., F.I.C.O.I. (Attached is photo for brochure)file://localhost/Users/mrpdmd7/Pictures/iPhoto%20Library/Masters/2003/Office%20Pictures/Dr.%20Pulaski%202.jpg

Target Market(s)

Adults, primarily senior adults.

Industry/Entity Type

Dental

```html
<!DOCTYPE html>
<html lang="en">
<head>
<meta charset="utf-8">
<title>Brookfield Dental Care – Implant FAQ</title>
<link href="https://fonts.googleapis.com/css2?family=Source+Sans+3:wght@400;600;700&display=swap" rel="stylesheet">
<style>
  :root {
    --teal: #74bfcb;
    --navy: #2c4e9c;
    --heading-blue: #2f5ba9;
    --q-blue: #4f8fc6;
    --text: #1d2742;
    --footer-bg: #e9f1f5;
    --paper: #ffffff;
  }
  * { margin: 0; padding: 0; box-sizing: border-box; }
  html, body { width: 925px; height: 1200px; overflow: hidden; background: var(--paper); }
  body { font-family: "Source Sans 3", "Myriad Pro", Arial, sans-serif; color: var(--text); position: relative; }

  .top-band { position: absolute; left: 0; top: 0; width: 925px; height: 51px; background: var(--teal); }
  .top-rule { position: absolute; left: 0; top: 58px; width: 925px; height: 11px; background: var(--navy); }

  .faq { position: absolute; left: 62px; top: 84px; width: 812px; font-size: 14.6px; line-height: 20px; }
  .faq .question { margin-top: 22px; }
  .faq .question:first-child { margin-top: 0; }
  .faq .answer { margin-top: 20px; text-align: justify; }
  .faq .answer p + p { text-indent: 56px; }
  .label { color: var(--q-blue); }

  .implant-art {
    position: absolute; left: 42px; top: 605px; width: 275px; height: 480px;
    background: linear-gradient(180deg, #f4f4f2 0%, #e9e7e4 26%, #d99a94 36%, #e9d8bd 52%, #dcc7a3 100%);
    border-radius: 6px;
  }

  .gallery-title {
    position: absolute; left: 333px; top: 626px; font-size: 53px; font-weight: 700;
    color: var(--heading-blue); line-height: 1; letter-spacing: -0.5px;
  }
  .gallery {
    position: absolute; left: 335px; top: 679px; width: 548px; height: 405px;
    background: var(--navy); padding: 8px;
    display: grid; grid-template-columns: 1fr 1fr; grid-template-rows: 1fr 1fr 1fr; gap: 3px;
  }
  .gallery .shot { background: linear-gradient(180deg, #b77f73 0%, #efe8dc 50%, #a6685f 100%); }

  .bottom-rule { position: absolute; left: 0; top: 1126px; width: 925px; height: 9px; background: var(--navy); }
  .footer {
    position: absolute; left: 0; top: 1135px; width: 925px; height: 65px; background: var(--footer-bg);
    display: flex; align-items: center; padding-left: 32px; font-size: 13px; color: var(--text);
  }
  .footer .sep { font-weight: 700; margin: 0 20px; }
  .footer .phone-label { font-weight: 700; }
</style>
</head>
<body>
  <div class="top-band"></div>
  <div class="top-rule"></div>

  <section class="faq">
    <p class="question"><span class="label">Q:</span> Do You Offer Any Warranties?</p>
    <div class="answer">
      <p><span class="label">A:</span> Yes. Even though dental implants have over a 95% success rate, there is still a very small chance that they won't completely bond. When this occurs, new implants are placed and the success rates for the replacement implants are even higher.</p>
      <p>If we replace your implant, we keep working from FREE until we get it right. The only thing you need to do is make sure you come in for your regularly scheduled visits so that we can keep your gums and teeth healthy, which will prevent most problems.</p>
    </div>

    <p class="question"><span class="label">Q:</span> What is the Cost of Implant Treatment?</p>
    <div class="answer">
      <p><span class="label">A:</span> Most people call and ask us, “How much is one implant going to cost?” The best way to determine actual cost is by coming in for a consultation and examination.</p>
      <p>The actual cost of implant treatment is based on a number of factors, such as the number of teeth being replaced, the type of treatment option recommended, and whether additional procedures are necessary to achieve the proper esthetic and functional results.</p>
    </div>

    <p class="question"><span class="label">Q:</span> Does Insurance Cover Dental Implant Treatment?</p>
    <div class="answer">
      <p><span class="label">A:</span> Insurance coverage depends on you individual policy. Most policies do not give substantial coverage.</p>
      <p>Although many companies exclude implants as a covered benefit, many of them will pay the same benefit they would cover for the lowest cost alternative treatment option (partials and dentures) and some for the diagnostic records.</p>
    </div>
  </section>

  <div class="implant-art" role="img" aria-label="Cross-section illustration of a dental implant with crown set in gum and bone"></div>

  <h2 class="gallery-title">before &amp; after</h2>
  <div class="gallery">
    <div class="shot" role="img" aria-label="Smile before treatment with missing teeth"></div>
    <div class="shot" role="img" aria-label="Smile after implant treatment"></div>
    <div class="shot" role="img" aria-label="Smile before treatment with a gap in front teeth"></div>
    <div class="shot" role="img" aria-label="Smile after implant treatment"></div>
    <div class="shot" role="img" aria-label="Smile before treatment with a missing tooth"></div>
    <div class="shot" role="img" aria-label="Smile after implant treatment"></div>
  </div>

  <div class="bottom-rule"></div>
  <footer class="footer">
    <span>Brookfield Dental Care, 218 Larchmont Avenue, Brookfield, PA 17342</span>
    <span class="sep">|</span>
    <span>www.brookfielddentalcare-example.com</span>
    <span class="sep">|</span>
    <span><span class="phone-label">phone</span> 717-482-6915</span>
  </footer>
</body>
</html>
```